Urine collection cup with and without sterile seal sticker

Hello. We need a urine cup label designed please with

Name:
Date of Birth:
Date:
Time:
Temp℃:
Specimen ID:

Product code: TUB-47
Volume markings (e.g., 30 mL, 60 mL, 90 mL).
Vela Drug Tests logo

Could you please provide one version with the additional sterile sticker extending to the top, and one version without the additional sterile sticker?

```html
<!DOCTYPE html>
<html lang="en">
<head>
<meta charset="utf-8">
<title>Vela Drug Tests – Urine Cup Labels</title>
<link href="https://fonts.googleapis.com/css2?family=Roboto:wght@400;500;700;900&display=swap" rel="stylesheet">
<style>
  :root {
    --navy: #0b1a5e;
    --ink: #13205f;
    --seal: #2b1f6d;
    --scale-bg: #e3f2fd;
    --stripe: #0a84d8;
    --brand-blue: #2a9be0;
    --paper: #ffffff;
  }
  * { margin: 0; padding: 0; box-sizing: border-box; }
  html, body { width: 1200px; height: 853px; overflow: hidden; background: var(--paper); }
  body { position: relative; font-family: "Roboto", sans-serif; color: var(--ink); }

  .version-title {
    position: absolute; top: 166px; width: 420px; text-align: center;
    font-weight: 900; font-size: 25px; letter-spacing: 0.2px; color: var(--navy);
  }
  .version-title--with { left: 122px; }
  .version-title--without { left: 664px; }

  .label {
    position: absolute; top: 222px; height: 532px;
    border: 1.5px solid var(--navy); border-radius: 14px; overflow: hidden;
    background: var(--paper);
  }
  .label--with { left: 86px; width: 484px; }
  .label--without { left: 625px; width: 485px; }

  .scale-column {
    position: absolute; top: 0; height: 457px; background: var(--scale-bg);
  }
  .label--with .scale-column { left: 304px; width: 100px; }
  .label--without .scale-column { left: 366px; right: 0; }

  .brand { position: absolute; left: 43px; top: 16px; display: flex; align-items: center; gap: 6px; }
  .brand-dot { width: 38px; height: 38px; border-radius: 50%; background: var(--brand-blue); }
  .brand-name { font-weight: 700; font-size: 28px; color: var(--navy); }

  .field {
    position: absolute; left: 24px; display: flex; align-items: flex-end;
    font-size: 20px; color: var(--ink);
  }
  .label--with .field { width: 260px; }
  .label--without .field { width: 322px; }
  .field-line { flex: 1; margin-left: 8px; border-bottom: 1.5px solid var(--ink); margin-bottom: 5px; }

  .mark { position: absolute; display: flex; align-items: center; font-size: 19px; color: var(--ink); }
  .mark-dash { width: 19px; height: 2px; background: var(--ink); margin-right: 9px; }
  .label--with .mark { left: 313px; }
  .label--without .mark { left: 376px; }

  .stripe { position: absolute; left: 0; right: 0; top: 457px; height: 9px; background: var(--stripe); }
  .footer {
    position: absolute; left: 0; right: 0; top: 466px; bottom: 0; background: var(--navy);
    color: #fff; font-size: 21px; padding: 16px 0 0 24px;
  }

  .seal-sticker {
    position: absolute; left: 490px; top: 90px; width: 80px; height: 598px;
    background: var(--seal); z-index: 2;
  }
  .seal-sticker text { fill: #fff; font-family: "Roboto", sans-serif; }
  .seal-word { font-weight: 900; font-size: 44px; }
  .seal-note { font-weight: 700; font-size: 15px; letter-spacing: 0.6px; }
</style>
</head>
<body>

  <h2 class="version-title version-title--with">WITH STERILE STICKER</h2>
  <h2 class="version-title version-title--without">WITHOUT STERILE STICKER</h2>

  <!-- Label with sterile seal -->
  <section class="label label--with">
    <div class="scale-column"></div>
    <div class="brand"><span class="brand-dot"></span><span class="brand-name">Vela Drug Tests</span></div>

    <div class="field" style="top:100px">Name:<span class="field-line"></span></div>
    <div class="field" style="top:155px">Date of Birth:<span class="field-line"></span></div>
    <div class="field" style="top:209px">Date:<span class="field-line"></span></div>
    <div class="field" style="top:264px">Time:<span class="field-line"></span></div>
    <div class="field" style="top:319px">Temp℃:<span class="field-line"></span></div>
    <div class="field" style="top:373px">Specimen ID:<span class="field-line"></span></div>

    <div class="mark" style="top:97px"><span class="mark-dash"></span>90 mL</div>
    <div class="mark" style="top:152px"><span class="mark-dash"></span></div>
    <div class="mark" style="top:208px"><span class="mark-dash"></span>60 mL</div>
    <div class="mark" style="top:264px"><span class="mark-dash"></span></div>
    <div class="mark" style="top:321px"><span class="mark-dash"></span>30 mL</div>

    <div class="stripe"></div>
    <div class="footer">Product code: TUB-47</div>
  </section>

  <div class="seal-sticker">
    <svg width="80" height="598" viewBox="0 0 80 598" aria-label="Sterile interior as long as seal remains intact">
      <text class="seal-word" transform="translate(26,168) rotate(90)" textLength="124" lengthAdjust="spacingAndGlyphs">STERILE</text>
      <text class="seal-note" transform="translate(43,319) rotate(90)" textLength="252" lengthAdjust="spacingAndGlyphs">INTERIOR AS LONG AS SEAL</text>
      <text class="seal-note" transform="translate(24,369) rotate(90)" textLength="143" lengthAdjust="spacingAndGlyphs">REMAINS INTACT</text>
    </svg>
  </div>

  <!-- Label without sterile seal -->
  <section class="label label--without">
    <div class="scale-column"></div>
    <div class="brand"><span class="brand-dot"></span><span class="brand-name">Vela Drug Tests</span></div>

    <div class="field" style="top:100px">Name:<span class="field-line"></span></div>
    <div class="field" style="top:155px">Date of Birth:<span class="field-line"></span></div>
    <div class="field" style="top:209px">Date:<span class="field-line"></span></div>
    <div class="field" style="top:264px">Time:<span class="field-line"></span></div>
    <div class="field" style="top:319px">Temp℃:<span class="field-line"></span></div>
    <div class="field" style="top:373px">Specimen ID:<span class="field-line"></span></div>

    <div class="mark" style="top:97px"><span class="mark-dash"></span>90 mL</div>
    <div class="mark" style="top:152px"><span class="mark-dash"></span></div>
    <div class="mark" style="top:208px"><span class="mark-dash"></span>60 mL</div>
    <div class="mark" style="top:264px"><span class="mark-dash"></span></div>
    <div class="mark" style="top:321px"><span class="mark-dash"></span>30 mL</div>

    <div class="stripe"></div>
    <div class="footer">Product code: TUB-47</div>
  </section>

</body>
</html>
```